Roofing company needs a door hanger designed.

Hello, I would like to have a door hanger designed for our roofing company in Orlando Florida. I have included information about us below and attached our logo. Please let me know if there is anything else you need? thank you.

BRIGHT HARBOR ROOFING
5417 Copper Meadow Blvd. Winter Park, FL 32795
Website: brightharborroofco.example
Email: info@brightharborroofco.example
Office phone #: 407.555.0146

Notes: In the state of Florida a roofing contractor must include their license number on all documentation and marketing materials. Lic#CCC1590827

Items I would like to add:
-CALL TODAY FOR A FREE ESTIMATE
-SCHEDULE YOUR FREE INSPECTION TODAY
-OUR SERVICES: ROOF REPLACEMENT, ROOF REPAIR, EMERGENCY SERVICES
-LICENSED & INSURED
OTHER SENTENCES / PARAGRAPHS IF NEEDED.
-We at Bright Harbor Roofing are dedicated to providing superior service.
-Driven to offer the highest quality and professional commercial and residential roofing solutions at a fair price.
-Our goal is to provide you with the best value possible!
-The best option not the highest priced option. Sometimes a small roof repair is all it takes to fix your roofing issues.
-Free roof inspections and proposals that are customized to your project to solve your roofing needs.

```html
<!DOCTYPE html>
<html lang="en">
<head>
<meta charset="utf-8">
<title>Bright Harbor Roofing – Door Hanger</title>
<link href="https://fonts.googleapis.com/css2?family=Montserrat:wght@400;500;600;700;800&display=swap" rel="stylesheet">
<style>
:root{
  --navy:#111a2b;
  --orange:#f7931e;
  --white:#ffffff;
  --page:#b3b3b3;
  --ink:#1a1f2b;
}
*{margin:0;padding:0;box-sizing:border-box}
html,body{width:976px;height:1200px;overflow:hidden;background:var(--page)}
body{position:relative;font-family:"Montserrat",sans-serif;color:var(--ink)}
.hanger{position:absolute;top:107px;width:638px;height:1754px;background:var(--white);transform:scale(.5622);transform-origin:0 0;overflow:hidden}
.hanger--front{left:100px}
.hanger--back{left:519px}
.abs{position:absolute}
.center{left:0;right:0;text-align:center}
.hero{position:absolute;left:0;top:0}
.brand{top:62px;display:flex;align-items:center;justify-content:center;gap:14px}
.brand__dot{width:34px;height:34px;border-radius:50%;background:var(--orange)}
.brand__name{font-weight:800;color:var(--navy);font-size:30px;line-height:1.05;letter-spacing:1px;text-align:left}
.headline{top:760px;font-size:70px;font-weight:800;color:var(--navy);letter-spacing:2px;line-height:1}
.subhead{top:842px;font-size:41px;font-weight:800;color:var(--navy);letter-spacing:1.5px;line-height:1}
.rule{left:254px;width:132px;top:891px;height:2px;background:var(--navy)}
.licensed{top:910px;font-size:31px;font-weight:600;color:var(--orange);letter-spacing:2.5px}
.services-title{left:160px;top:985px;width:318px;height:43px;border:2px solid var(--orange);font-size:28px;font-weight:500;color:var(--navy);letter-spacing:1.5px;display:flex;align-items:center;justify-content:center}
.service-link{top:1110px;height:1.5px;width:81px;background:var(--orange)}
.service{top:1057px;width:200px;text-align:center}
.service__icon{position:relative;width:98px;height:98px;margin:0 auto 0 51px}
.service__icon::before{content:"";position:absolute;left:0;top:0;width:87px;height:87px;border:3px solid var(--orange)}
.service__icon .tile{position:absolute;left:11px;top:11px;width:87px;height:87px;background:var(--navy);display:flex;align-items:center;justify-content:center}
.service__label{margin-top:18px;font-size:21px;font-weight:500;letter-spacing:2px;line-height:24px;color:var(--navy)}
.license-line{left:0;right:0;top:1265px;height:1px;background:var(--orange)}
.license{left:64px;width:511px;top:1240px;height:50px;background:var(--navy);color:var(--white);font-size:25px;font-weight:600;letter-spacing:1px;white-space:nowrap;display:flex;align-items:center;justify-content:center}
.license::before,.license::after{content:"";position:absolute;top:24px;width:30px;height:1.5px;background:var(--white)}
.license::before{left:12px}
.license::after{right:12px}
.cta{left:0;right:0;top:1323px;height:179px;background:var(--orange);text-align:center;color:var(--white)}
.cta__lead{margin-top:14px;font-size:27px;font-weight:500;letter-spacing:2.5px;line-height:32px}
.cta__est{font-size:31px;font-weight:500;letter-spacing:3px;display:flex;align-items:center;justify-content:center;gap:18px;line-height:32px}
.cta__est::before,.cta__est::after{content:"";width:52px;height:1.5px;background:var(--navy)}
.phone{position:absolute;left:64px;width:511px;top:94px;height:62px;border:1.5px solid var(--white);color:var(--navy);font-size:46px;font-weight:800;letter-spacing:3px;display:flex;align-items:center;justify-content:center}
.footer{left:0;right:0;top:1502px;bottom:0;background:var(--navy);color:var(--white)}
.footer__box{position:absolute;left:64px;width:511px;top:22px;height:130px;border:1.5px solid var(--orange)}
.footer__line{position:absolute;top:52px;height:1px;width:125px;background:var(--white)}
.footer__name{position:absolute;left:0;right:0;top:37px;text-align:center;color:var(--orange);font-size:23px;font-weight:500;letter-spacing:1.5px;line-height:30px;white-space:nowrap}
.footer__web{position:absolute;left:0;right:0;top:78px;text-align:center;font-size:21px;letter-spacing:1px;line-height:34px;white-space:nowrap}
.footer__addr{position:absolute;left:0;right:0;top:170px;text-align:center;font-size:21px;letter-spacing:1px;line-height:27px}
.footer__zip{display:flex;align-items:center;justify-content:center;gap:18px}
.footer__zip::before,.footer__zip::after{content:"";width:58px;height:1px;background:var(--orange)}
.why-title{left:64px;width:510px;top:777px;height:60px;border:3px solid var(--navy);color:var(--orange);font-size:40px;font-weight:800;letter-spacing:2px;display:flex;align-items:center;justify-content:center}
.reason{left:58px;width:530px;display:flex;gap:20px;align-items:flex-start}
.reason__icon{position:relative;flex:0 0 72px;height:72px}
.reason__icon::before{content:"";position:absolute;left:0;top:0;width:66px;height:66px;border:2px solid var(--orange)}
.reason__icon .tile{position:absolute;left:6px;top:6px;width:66px;height:66px;background:var(--navy);display:flex;align-items:center;justify-content:center}
.reason__text{font-size:19px;line-height:24px;letter-spacing:.3px;color:var(--navy);padding-top:8px}
</style>
</head>
<body>

<section class="hanger hanger--front">
  <svg class="hero" width="638" height="740" viewBox="0 0 638 740">
    <defs>
      <linearGradient id="roofPhoto" x1="0" y1="0" x2="1" y2="1">
        <stop offset="0" stop-color="#2a2d33"/>
        <stop offset=".45" stop-color="#3a3c40"/>
        <stop offset=".75" stop-color="#8a5a35"/>
        <stop offset="1" stop-color="#b07a48"/>
      </linearGradient>
    </defs>
    <g role="img" aria-label="Photo of two roofers in hard hats installing a dark metal roof on a timber house">
      <polygon points="0,122 319,222 638,122 638,600 319,698 0,600" fill="url(#roofPhoto)"/>
    </g>
    <polygon points="0,600 319,698 638,600 638,625 319,722 0,625" fill="var(--orange)"/>
    <rect x="0" y="350" width="320" height="74" fill="var(--page)"/>
    <circle cx="319" cy="387" r="118" fill="var(--page)"/>
  </svg>
  <div class="abs center brand"><span class="brand__dot"></span><span class="brand__name">BRIGHT HARBOR<br>ROOFING</span></div>

  <h1 class="abs center headline">RESIDENTIAL</h1>
  <h2 class="abs center subhead">ROOFING AND REPAIR</h2>
  <div class="abs rule"></div>
  <p class="abs center licensed">LICENSED &amp; INSURED</p>
  <div class="abs services-title">OUR SERVICES</div>

  <div class="abs service-link" style="left:172px"></div>
  <div class="abs service-link" style="left:375px"></div>
  <div class="abs service" style="left:16px">
    <div class="service__icon"><div class="tile">
      <svg width="50" height="50" viewBox="0 0 50 50" fill="none" stroke="#fff" stroke-width="3" stroke-linejoin="round"><path d="M5 24 25 6l20 18M10 20v24h30V20"/><path d="M20 44V32h10v12"/></svg>
    </div></div>
    <p class="service__label">ROOF<br>REPLACEMENT</p>
  </div>
  <div class="abs service" style="left:219px">
    <div class="service__icon"><div class="tile">
      <svg width="50" height="50" viewBox="0 0 50 50" fill="none" stroke="#fff" stroke-width="3" stroke-linejoin="round"><path d="M10 8h24l6 6H34v-2H12z"/><path d="M22 14v30h5V14"/></svg>
    </div></div>
    <p class="service__label">ROOF<br>REPAIRING</p>
  </div>
  <div class="abs service" style="left:422px">
    <div class="service__icon"><div class="tile">
      <svg width="50" height="50" viewBox="0 0 50 50" fill="none" stroke="#fff" stroke-width="2.5"><rect x="13" y="4" width="24" height="42" rx="2"/><path d="M13 38h24M13 11h24M25 18v10M20 23h10"/></svg>
    </div></div>
    <p class="service__label">EMERGENCY<br>SERVICES</p>
  </div>

  <div class="abs license-line"></div>
  <div class="abs license">FL LICENSE - CCC1590827</div>

  <div class="abs cta">
    <p class="cta__lead">CALL TODAY FOR A FREE</p>
    <p class="cta__est">ESTIMATE</p>
    <div class="phone">407-555-0146</div>
  </div>

  <footer class="abs footer">
    <div class="footer__line" style="left:0"></div>
    <div class="footer__line" style="right:0"></div>
    <div class="footer__box"></div>
    <p class="footer__name">BRIGHT HARBOR ROOFING</p>
    <p class="footer__web">www.brightharborroofco.example<br>info@brightharborroofco.example</p>
    <p class="footer__addr">5417 Copper Meadow Blvd. Winter Park,<span class="footer__zip">FL 32795</span></p>
  </footer>
</section>

<section class="hanger hanger--back">
  <svg class="hero" width="638" height="740" viewBox="0 0 638 740">
    <defs>
      <linearGradient id="tilePhoto" x1="1" y1="0" x2="0" y2="1">
        <stop offset="0" stop-color="#3a8fd6"/>
        <stop offset=".35" stop-color="#9cc6e8"/>
        <stop offset=".55" stop-color="#3b2a2c"/>
        <stop offset="1" stop-color="#241b1f"/>
      </linearGradient>
    </defs>
    <g role="img" aria-label="Photo of a dark brown tiled roof against a clear blue sky">
      <polygon points="0,122 319,222 638,122 638,600 319,698 0,600" fill="url(#tilePhoto)"/>
    </g>
    <polygon points="0,600 319,698 638,600 638,625 319,722 0,625" fill="var(--orange)"/>
    <rect x="318" y="350" width="320" height="74" fill="var(--page)"/>
    <circle cx="319" cy="387" r="118" fill="var(--page)"/>
  </svg>
  <div class="abs center brand"><span class="brand__dot"></span><span class="brand__name">BRIGHT HARBOR<br>ROOFING</span></div>

  <h2 class="abs why-title">WHY CHOOSE US</h2>

  <div class="abs reason" style="top:866px">
    <div class="reason__icon"><div class="tile"><svg width="42" height="42" viewBox="0 0 42 42" fill="none" stroke="#fff" stroke-width="2"><path d="M12 6l4 5 5-7 5 7 4-5v10H12z"/><path d="M4 30h8l8 3h12l6-6M4 36h10l8 2h10"/></svg></div></div>
    <p class="reason__text">We at Bright Harbor Roofing are dedicated to providing superior service.</p>
  </div>
  <div class="abs reason" style="top:954px">
    <div class="reason__icon"><div class="tile"><svg width="42" height="42" viewBox="0 0 42 42" fill="none" stroke="#fff" stroke-width="2"><path d="M21 4v32M8 10h26M14 36h14"/><path d="M8 10l-5 12h10zM34 10l-5 12h10z"/></svg></div></div>
    <p class="reason__text">Driven to offer the highest quality and professional commercial and residential roofing solutions at a fair price.</p>
  </div>
  <div class="abs reason" style="top:1042px">
    <div class="reason__icon"><div class="tile"><svg width="44" height="44" viewBox="0 0 44 44" fill="none" stroke="#fff" stroke-width="2"><path d="M22 3l5 5 7-1 1 7 5 5-4 6 2 7-7 2-3 6-6-3-6 3-3-6-7-2 2-7-4-6 5-5 1-7 7 1z"/><circle cx="22" cy="22" r="10"/></svg></div></div>
    <p class="reason__text">Our goal is to provide you with the best value possible!</p>
  </div>
  <div class="abs reason" style="top:1130px">
    <div class="reason__icon"><div class="tile"><svg width="42" height="42" viewBox="0 0 42 42" fill="none" stroke="#fff" stroke-width="2"><path d="M16 12h10l-2-6h-6zM16 12c-8 6-10 14-6 20 3 4 15 4 18 0 4-6 2-14-6-20"/><path d="M36 14v20M32 30l4 4 4-4"/></svg></div></div>
    <p class="reason__text">The best option not the highest priced option. Sometimes a small roof repair is all it takes to fix your roofing issues.</p>
  </div>
  <div class="abs reason" style="top:1217px">
    <div class="reason__icon"><div class="tile"><svg width="44" height="44" viewBox="0 0 44 44" fill="none" stroke="#fff" stroke-width="2"><circle cx="22" cy="22" r="18"/><circle cx="22" cy="22" r="14"/><text x="22" y="26" text-anchor="middle" fill="#fff" stroke="none" font-family="Montserrat,sans-serif" font-size="10" font-weight="700">FREE</text></svg></div></div>
    <p class="reason__text">Free roof inspections and proposals that are customized to your project to solve your roofing needs.</p>
  </div>

  <div class="abs cta">
    <p class="cta__lead">CALL TODAY FOR A FREE</p>
    <p class="cta__est">ESTIMATE</p>
    <div class="phone">407-555-0146</div>
  </div>

  <footer class="abs footer">
    <div class="footer__line" style="left:0"></div>
    <div class="footer__line" style="right:0"></div>
    <div class="footer__box"></div>
    <p class="footer__name">BRIGHT HARBOR ROOFING</p>
    <p class="footer__web">www.brightharborroofco.example<br>info@brightharborroofco.example</p>
    <p class="footer__addr">5417 Copper Meadow Blvd. Winter Park,<span class="footer__zip">FL 32795</span></p>
  </footer>
</section>

</body>
</html>
```